Buff & Gleam

polished concrete and epoxy coatings flooring company

Target Market(s)

Industrial commercial

Industry/Entity Type

Industrial flooring contractor

Contact Information for Business Card

POLISHED CONCRETE • EPOXY COATING • TERRAZZO RESTORATION • SHOT BLASTING • SURFACE PREPARATION • JOINT FILLING • TILE/ CARPET /GLUE REMOVAL

Colors
0054AA
0677BA
7BADD7
CADEEF
E8F1F8

Requirements
Must have
• email buffandgleamfloors@mailbrook.example Address 47215 Tallowmere Rd, Kellbrook, WY 82990. Name Ray Tulvin. Services Polished concrete- Epoxy Coatings- Terrazzo restoration-surface preparation- safety striping- joint filling- tile/ carpet/ glue removal phone number 555-700-3926 email buffandgleamfloors.example
Nice to have
• Instagram Facebook logo maybe smaller in the corner

```html
<!DOCTYPE html>
<html lang="en">
<head>
<meta charset="utf-8">
<title>Buff &amp; Gleam — Business Card</title>
<link rel="stylesheet" href="https://fonts.googleapis.com/css2?family=Cinzel:wght@500&family=Lato:wght@400;700&family=Montserrat:wght@500&display=swap">
<style>
  :root {
    --backdrop: #8a8a8a;
    --card-dark: #1c1c1d;
    --blue-deep: #0054AA;
    --blue-mid: #0677BA;
    --blue-soft: #7BADD7;
    --blue-pale: #CADEEF;
    --blue-mist: #E8F1F8;
    --text-light: #d9d9d9;
    --white: #ffffff;
  }
  * { box-sizing: border-box; margin: 0; padding: 0; }
  html, body { width: 1200px; height: 801px; overflow: hidden; }
  body {
    background: var(--backdrop);
    position: relative;
    font-family: "Lato", sans-serif;
  }
  .card {
    position: absolute;
    top: 246px;
    width: 540px;
    height: 309px;
    border-radius: 24px;
    overflow: hidden;
    box-shadow: 0 14px 30px rgba(0,0,0,0.35);
  }
  .card-front { left: 40px; background: var(--card-dark); }
  .card-back {
    left: 620px;
    background: linear-gradient(225deg, var(--blue-deep) 0%, var(--blue-deep) 45%, var(--blue-mid) 75%, var(--blue-soft) 100%);
  }
  .brand-name {
    position: absolute;
    top: 134px;
    width: 200px;
    text-align: center;
    font-family: "Lato", sans-serif;
    font-weight: 700;
    font-size: 30px;
    letter-spacing: 0.5px;
    white-space: nowrap;
  }
  .card-front .brand-name { left: 30px; color: var(--blue-mid); }
  .card-back .brand-name { left: 28px; color: var(--white); }
  .divider {
    position: absolute;
    top: 62px;
    width: 1.5px;
    height: 185px;
  }
  .card-front .divider { left: 252px; background: var(--blue-mid); }
  .card-back .divider { left: 250px; background: var(--white); }
  .contact { position: absolute; left: 274px; top: 70px; }
  .person-name {
    font-family: "Cinzel", serif;
    font-weight: 500;
    font-size: 27px;
    color: var(--blue-mid);
    letter-spacing: 1px;
    margin-bottom: 14px;
  }
  .contact-row {
    display: flex;
    align-items: flex-start;
    gap: 9px;
    font-size: 12px;
    line-height: 17px;
    color: var(--text-light);
    margin-bottom: 5px;
  }
  .contact-row svg { flex: none; width: 13px; height: 13px; margin-top: 2px; fill: var(--blue-soft); }
  .services {
    position: absolute;
    left: 276px;
    top: 70px;
    list-style: none;
    font-family: "Montserrat", sans-serif;
    font-weight: 500;
    font-size: 12.5px;
    color: var(--white);
    letter-spacing: 0.4px;
  }
  .services li { display: flex; align-items: center; gap: 10px; height: 23px; }
  .services svg { width: 11px; height: 11px; }
  .social {
    position: absolute;
    right: 30px;
    bottom: 26px;
    display: flex;
    gap: 8px;
  }
  .social span {
    width: 24px;
    height: 24px;
    border: 1.5px solid var(--white);
    border-radius: 50%;
  }
</style>
</head>
<body>
  <section class="card card-front" aria-label="Business card front">
    <div class="brand-name">Buff &amp; Gleam</div>
    <div class="divider"></div>
    <div class="contact">
      <div class="person-name">RAY TULVIN</div>
      <div class="contact-row">
        <svg viewBox="0 0 24 24" aria-hidden="true"><path d="M12 2a7 7 0 0 0-7 7c0 5 7 13 7 13s7-8 7-13a7 7 0 0 0-7-7zm0 9.5A2.5 2.5 0 1 1 12 6.5a2.5 2.5 0 0 1 0 5z"/></svg>
        <span>47215 Tallowmere Rd<br>Kellbrook, WY 82990</span>
      </div>
      <div class="contact-row">
        <svg viewBox="0 0 24 24" aria-hidden="true"><path d="M6.6 10.8a15.1 15.1 0 0 0 6.6 6.6l2.2-2.2a1 1 0 0 1 1-.25 11.4 11.4 0 0 0 3.6.57 1 1 0 0 1 1 1V20a1 1 0 0 1-1 1A17 17 0 0 1 3 4a1 1 0 0 1 1-1h3.5a1 1 0 0 1 1 1c0 1.25.2 2.45.57 3.6a1 1 0 0 1-.25 1z"/></svg>
        <span>555-700-3926</span>
      </div>
      <div class="contact-row">
        <svg viewBox="0 0 24 24" aria-hidden="true"><path d="M2 5h20v14H2zm2 2v.5l8 5 8-5V7z"/></svg>
        <span>buffandgleamfloors@mailbrook.example</span>
      </div>
      <div class="contact-row">
        <svg viewBox="0 0 24 24" aria-hidden="true"><path d="M12 2a10 10 0 1 0 0 20 10 10 0 0 0 0-20zm6.9 6h-3a15 15 0 0 0-1.3-3.9A8 8 0 0 1 18.9 8zM12 4a13 13 0 0 1 1.9 4h-3.8A13 13 0 0 1 12 4zM4.3 14a8 8 0 0 1 0-4h3.4a16 16 0 0 0 0 4zm.8 2h3a15 15 0 0 0 1.3 3.9A8 8 0 0 1 5.1 16zm3-8h-3a8 8 0 0 1 4.3-3.9A15 15 0 0 0 8.1 8zM12 20a13 13 0 0 1-1.9-4h3.8A13 13 0 0 1 12 20zm2.3-6H9.7a14 14 0 0 1 0-4h4.6a14 14 0 0 1 0 4zm.3 5.9a15 15 0 0 0 1.3-3.9h3a8 8 0 0 1-4.3 3.9zm1.7-5.9a16 16 0 0 0 0-4h3.4a8 8 0 0 1 0 4z"/></svg>
        <span>buffandgleamfloors.example</span>
      </div>
    </div>
  </section>

  <section class="card card-back" aria-label="Business card back">
    <div class="brand-name">Buff &amp; Gleam</div>
    <div class="divider"></div>
    <ul class="services">
      <li><svg viewBox="0 0 12 12" aria-hidden="true"><path d="M1 6.5l3 3 7-7" fill="none" stroke="#fff" stroke-width="2.2"/></svg>POLISHED CONCRETE</li>
      <li><svg viewBox="0 0 12 12" aria-hidden="true"><path d="M1 6.5l3 3 7-7" fill="none" stroke="#fff" stroke-width="2.2"/></svg>EPOXY COATING</li>
      <li><svg viewBox="0 0 12 12" aria-hidden="true"><path d="M1 6.5l3 3 7-7" fill="none" stroke="#fff" stroke-width="2.2"/></svg>TERRAZZO RESTORATION</li>
      <li><svg viewBox="0 0 12 12" aria-hidden="true"><path d="M1 6.5l3 3 7-7" fill="none" stroke="#fff" stroke-width="2.2"/></svg>SHOT BLASTING</li>
      <li><svg viewBox="0 0 12 12" aria-hidden="true"><path d="M1 6.5l3 3 7-7" fill="none" stroke="#fff" stroke-width="2.2"/></svg>SURFACE PREPARATION</li>
      <li><svg viewBox="0 0 12 12" aria-hidden="true"><path d="M1 6.5l3 3 7-7" fill="none" stroke="#fff" stroke-width="2.2"/></svg>JOINT FILLING</li>
      <li><svg viewBox="0 0 12 12" aria-hidden="true"><path d="M1 6.5l3 3 7-7" fill="none" stroke="#fff" stroke-width="2.2"/></svg>TILE/ CARPET /GLUE REMOVAL</li>
    </ul>
    <div class="social" aria-label="Social media links">
      <span></span><span></span>
    </div>
  </section>
</body>
</html>
```